依頼詳細
米袋パッケージデザインの依頼をさせて頂きます。
今回、特に希望する方向性はございません。

自由度がかなり高く、曖昧な部分がある為デザインが難しいかと思われますが、
どうか力をお貸しください。

・高級感、シンプルさ、オシャレな感じ、ポップな感じ、
そよ凪や宵月の調べ・岳兵衛などの統一デザインっぽさ、
など方向性は自由です。
・洋風、和風など自由です。
・写真、イラスト、フォント自由です。筆文字可。(版権等にご注意ください。)
・色も自由です。金色銀色使用可能です。

良いと思うデザイン例
・コンセプトやデザインに一捻りあるもの。
(絶対に必要というわけではありません。)
・特別感。(絶対に必要というわけではありません。)

悪いと思うデザイン例
・スーパーによく置いてあるような安っぽい感じ。

■デザイン上に必ず入れて欲しいもの■
※すべて「」は必要ありません。

・「新潟県産」※新潟や新潟産でもかまいません。
・「こしひかり」※カタカナでもかまいません。
・「5kg」
・「中のお米が見える部分」

印刷適正・文字などはデザイン決定後こちらで調整致しますので
背景や全体のデザインイメージを重要視します。

・修正作業をお願いすることはありません。
・ご提案をして頂く際に、袋に印刷されたように見える
擬似実物処理(立体)などは不要です。
平面画像のみで公平に判断したいと考えております。
記載項目
サイズ:W300mm×H470mm
グラビア印刷/ラミネート加工

```html
<!DOCTYPE html>
<html lang="ja">
<head>
<meta charset="utf-8">
<title>新潟県産こしひかり 5kg</title>
<link rel="stylesheet" href="https://fonts.googleapis.com/css2?family=Noto+Sans+JP:wght@900&family=Noto+Serif:ital,wght@1,400&display=swap">
<style>
  :root {
    --paper: #ffffff;
    --sky: #8fd0ef;
    --gold-dark: #6e5a22;
    --gold-mid: #b39a54;
    --gold-light: #d9c98c;
    --rice: #e4dccd;
    --ink: #111111;
  }
  html, body {
    margin: 0;
    padding: 0;
    overflow: hidden;
    background: var(--paper);
  }
  .bag {
    position: relative;
    width: 768px;
    height: 1200px;
    background: var(--paper);
    overflow: hidden;
  }
  .bands {
    position: absolute;
    inset: 0;
  }
  .title {
    position: absolute;
    top: 254px;
    margin: 0;
    writing-mode: vertical-rl;
    font-family: "Noto Sans JP", sans-serif;
    font-weight: 900;
    color: var(--ink);
    line-height: 1;
  }
  .title--origin {
    left: 456px;
    font-size: 146px;
    letter-spacing: 6px;
  }
  .title--variety {
    left: 300px;
    font-size: 148px;
    letter-spacing: 4px;
  }
  .weight {
    position: absolute;
    left: 106px;
    top: 858px;
    margin: 0;
    font-family: "Noto Serif", serif;
    font-style: italic;
    font-size: 82px;
    color: var(--ink);
    line-height: 1;
  }
</style>
</head>
<body>
  <main class="bag">
    <svg class="bands" width="768" height="1200" viewBox="0 0 768 1200" aria-hidden="true">
      <defs>
        <linearGradient id="gold" x1="0" y1="0" x2="1" y2="0">
          <stop offset="0" stop-color="var(--gold-dark)"/>
          <stop offset="0.45" stop-color="var(--gold-light)"/>
          <stop offset="0.7" stop-color="var(--gold-mid)"/>
          <stop offset="1" stop-color="var(--gold-dark)"/>
        </linearGradient>
      </defs>
      <polygon class="band band--gold" fill="url(#gold)" points="0,243 768,90 768,218 0,370"/>
      <polygon class="band band--sky" fill="var(--sky)" points="0,390 768,236 768,358 0,512"/>
      <polygon class="band band--gold" fill="url(#gold)" points="0,620 768,466 768,586 0,735"/>
      <polygon class="band band--sky" fill="var(--sky)" points="0,1022 768,866 768,976 0,1132"/>
      <circle class="rice-window" cx="157" cy="660" r="107" fill="var(--rice)"/>
    </svg>
    <h1 class="title title--origin">新潟県産</h1>
    <h2 class="title title--variety">こしひかり</h2>
    <p class="weight">5kg</p>
  </main>
</body>
</html>
```